Visitenkarten-Design für Garten- und Landschaftspflege
Karvan Meltis setzte meine Vorstellungen absolut super um ich kann Ihn nur weiter empfehlen. vielen dank
Zielgruppe
Baumpflege, Baumfällung, Garten und Landschaftspflege meine zielgruppe sind Privatpersonen im alter von 20-100Jahren
Aufgabenstellung
Sehr geehrte Damen und Herren, die visitenkarte sollte die angaben so enthalten wie sie auf der von mir gestallteten Visitenkarten sind ( meine ist kein maß der Dinge). Ich habe mein Logo leider nur als 3.jpg Datei. Das Logo darf im Design erändert werden aber bitte nur Feinheiten ansonsten stehen ihnen alle türen offen um kreativ zu sein.
mit freundlichen Grüßen Jonas Wendtholm

```html
<!DOCTYPE html>
<html lang="de">
<head>
<meta charset="utf-8">
<title>Visitenkarte Baumpflege Wendtholm</title>
<link rel="stylesheet" href="https://fonts.googleapis.com/css2?family=Open+Sans:wght@400;800&display=swap">
<style>
  :root {
    --green: #99c011;
    --ink: #1c1c1c;
    --paper: #ffffff;
    --backdrop: #e9e9e7;
    --tree-tone: linear-gradient(180deg, #3a3a3a 0%, #1c1c1c 100%);
  }
  * { box-sizing: border-box; margin: 0; padding: 0; }
  html, body { width: 1200px; height: 520px; overflow: hidden; }
  body {
    background: var(--backdrop);
    font-family: "Open Sans", Arial, sans-serif;
    position: relative;
  }
  .card {
    position: absolute;
    top: 78px;
    width: 560px;
    height: 363px;
    background: var(--paper);
    overflow: hidden;
    box-shadow: 0 2px 8px rgba(0,0,0,.12);
  }
  .card--front { left: 28px; }
  .card--back { left: 612px; }

  .band {
    position: absolute;
    left: 0; right: 0; bottom: 0;
    background: var(--green);
    border-top: 7px solid var(--ink);
  }
  .card--front .band { top: 193px; }
  .card--back .band { top: 253px; }

  .illustration {
    position: absolute;
    background: var(--tree-tone);
    border-radius: 48% 52% 6% 6% / 60% 60% 6% 6%;
  }
  .card--front .illustration { left: 50px; top: 36px; width: 210px; height: 160px; }
  .card--back .illustration { left: 300px; top: 95px; width: 210px; height: 160px; }

  .heading { font-weight: 800; color: var(--green); font-size: 16px; line-height: 21px; }
  .text { font-weight: 400; color: var(--green); font-size: 15px; line-height: 21px; }
  .on-band .heading, .on-band .text { color: var(--paper); }

  .identity { position: absolute; left: 297px; top: 42px; }
  .contact { position: absolute; left: 300px; top: 236px; }

  .brand {
    position: absolute;
    left: 45px; top: 212px;
    display: flex; align-items: flex-start; gap: 8px;
    font-weight: 800; font-size: 20px; line-height: 23px;
    color: var(--ink);
  }
  .brand-mark { width: 14px; height: 14px; background: var(--ink); flex: none; margin-top: 5px; }

  .services { position: absolute; left: 42px; top: 22px; list-style: none; }
  .services li { padding-left: 10px; position: relative; }
  .services li::before { content: "·"; position: absolute; left: 0; }
  .services .services-title { padding-left: 0; }
  .services .services-title::before,
  .services .cont::before { content: ""; }

  .extra { position: absolute; left: 45px; top: 286px; }
</style>
</head>
<body>
  <section class="card card--front">
    <div class="illustration" role="img" aria-label="Schwarze Silhouette eines großen Laubbaums mit Holzzaun auf einer Wiesenkante"></div>
    <div class="identity">
      <p class="heading">Jonas Wendtholm</p>
      <p class="text">Fachagrarwirt Baumpflege/</p>
      <p class="text">Baumsanierung</p>
      <p class="text">Lindenweg 4</p>
      <p class="text">85600 Eichenau</p>
    </div>
    <div class="band"></div>
    <div class="brand"><span class="brand-mark"></span><span>Baumpflege<br>Wendtholm</span></div>
    <div class="contact on-band">
      <p class="heading">Kontakt</p>
      <p class="text">Tel.: 0170/5550123</p>
      <p class="text">www.baumpflege-wendtholm.de</p>
      <p class="text">kontakt@baumpflege-wendtholm.de</p>
    </div>
  </section>

  <section class="card card--back">
    <div class="illustration" role="img" aria-label="Schwarze Silhouette eines großen Laubbaums mit Holzzaun auf einer Wiesenkante"></div>
    <div class="band"></div>
    <ul class="services text">
      <li class="heading services-title">Unsere Leistungen</li>
      <li>Neupflanzungen</li>
      <li>Herstellen der Verkehrssicherheit von Bäumen</li>
      <li>Kronenrückschnitt</li>
      <li class="cont">(Einkürzung und Kronenpflege</li>
      <li>Prüfen von Bäumen auf</li>
      <li class="cont">Standsicherheit</li>
      <li>Fällung von Bäumen</li>
      <li>Obstbaumschnitt</li>
      <li>Fräsen von Wurzelstöcken</li>
    </ul>
    <div class="extra on-band">
      <p class="heading">Außerdem:</p>
      <p class="text">Aufbau und Anfertigung von Gartenhäusern nach Maß</p>
    </div>
  </section>
</body>
</html>
```